RW Frameworks Inc Business cards

We need business cards using our existing logo but slightly modified. Right now the logo says RW Framework Masonry. We want to keep the RW part of the design, but replace the Framework Masonry portion with "FRAMEWORKS". Please see the attached file.
Ideally this would be a blank template so we can add Different Names, titles, and phone numbers later.
On the one side we want only the logo and on the other side the detail. I'm attaching an example for you to see.
Please reach out with any other questions. Our address and other details will be given out once we find a design we like.

Target Market(s)

Construction Industry

```html
<!DOCTYPE html>
<html lang="en">
<head>
<meta charset="utf-8">
<title>RW Frameworks Inc – Business Cards</title>
<link rel="stylesheet" href="https://fonts.googleapis.com/css2?family=Arimo:ital,wght@0,400;0,700;1,700&family=Maven+Pro:wght@600&display=swap">
<style>
  :root {
    --brand-blue: #1175bf;
    --name-blue: #1a72b8;
    --back-blue: #0f78bf;
    --logo-light: #2fd6f2;
    --steel-grey: #808285;
    --text-grey: #4d4f52;
    --card-white: #ffffff;
    --page-bg: #e9eaec;
  }
  html, body {
    margin: 0;
    padding: 0;
    width: 1125px;
    height: 1200px;
    overflow: hidden;
    background: var(--page-bg);
  }
  .sheet {
    position: relative;
    width: 1125px;
    height: 1200px;
  }
  .card {
    position: absolute;
    left: 150px;
    width: 825px;
    height: 470px;
    box-shadow: 0 4px 14px rgba(0, 0, 0, 0.22);
  }
  .card--front { top: 98px; background: var(--card-white); }
  .card--back { top: 631px; background: var(--back-blue); }
  .card svg { display: block; width: 825px; height: 470px; }

  .wordmark { font-family: "Arimo", Arial, sans-serif; font-weight: 700; }
  .wordmark--front { fill: var(--brand-blue); }
  .wordmark--back { fill: var(--logo-light); }

  .holder-name { font-family: "Maven Pro", "Arimo", sans-serif; font-weight: 600; font-size: 25px; fill: var(--name-blue); letter-spacing: 0.3px; }
  .holder-title { font-family: "Arimo", Arial, sans-serif; font-weight: 700; font-size: 17px; fill: var(--steel-grey); }
  .contact-line { font-family: "Arimo", Arial, sans-serif; font-size: 17px; fill: var(--text-grey); }
  .contact-icon { fill: var(--brand-blue); }
  .divider { stroke: var(--steel-grey); stroke-width: 1.2; }
  .band-blue { fill: var(--brand-blue); }
  .band-grey { fill: var(--steel-grey); }
  .web-address { font-family: "Arimo", Arial, sans-serif; font-weight: 700; font-style: italic; font-size: 18px; fill: var(--card-white); }
</style>
</head>
<body>
<main class="sheet">

  <section class="card card--front" aria-label="Business card front">
    <svg viewBox="0 0 800 456" xmlns="http://www.w3.org/2000/svg">
      <g class="wordmark wordmark--front" aria-label="RW Frameworks">
        <text x="126" y="254" font-size="112" letter-spacing="2">RW</text>
        <text x="128" y="298" font-size="38" letter-spacing="4.5">Frameworks</text>
      </g>

      <line class="divider" x1="420" y1="158" x2="420" y2="300"/>

      <text class="holder-name" x="455" y="176">DANIEL CARTER</text>
      <text class="holder-title" x="457" y="200">President</text>

      <g class="contact">
        <path class="contact-icon" d="M461 238c1 0 2 1 3 3l-1 2c1 2 3 4 5 5l2-1c2 1 3 2 3 3 0 1-1 2-3 2-5-1-10-6-11-11 0-2 1-3 2-3z"/>
        <text class="contact-line" x="482" y="250">555-214-7390</text>

        <rect class="contact-icon" x="461" y="258" width="9" height="15" rx="1.5"/>
        <rect x="462.8" y="260" width="5.4" height="9" fill="#fff"/>
        <text class="contact-line" x="482" y="273">555-618-2043</text>

        <rect class="contact-icon" x="460" y="287" width="12" height="8"/>
        <path d="M460 287l6 4.5 6-4.5" fill="none" stroke="#fff" stroke-width="1.2"/>
        <text class="contact-line" x="482" y="295">info@rwframeworks.com</text>
      </g>

      <polygon class="band-blue" points="0,433 440,433 424,456 0,456"/>
      <polygon class="band-grey" points="482,415 800,415 800,456 446,456"/>
      <text class="web-address" x="535" y="441">www.rwframeworks</text>
    </svg>
  </section>

  <section class="card card--back" aria-label="Business card back">
    <svg viewBox="0 0 800 456" xmlns="http://www.w3.org/2000/svg">
      <g class="wordmark wordmark--back" aria-label="RW Frameworks">
        <text x="400" y="256" font-size="112" text-anchor="middle" letter-spacing="2">RW</text>
        <text x="400" y="304" font-size="38" text-anchor="middle" letter-spacing="4.5">Frameworks</text>
      </g>
    </svg>
  </section>

</main>
</body>
</html>
```